New Business Card Design Project

Details for my new Business Card Design Project will be added soon. Like a nice simple design

Target Market(s)

Home improvement

Industry/Entity Type

Home Improvement

Contact Information for Business Card

Roofing siding gutters additions garages decks

Requirements
Must have
• Phone 5074629183
• Email morvantgc@quellmail.com

```html
<!DOCTYPE html>
<html lang="en">
<head>
<meta charset="utf-8">
<title>Business Card</title>
<link rel="stylesheet" href="https://fonts.googleapis.com/css2?family=Arimo:wght@700&display=swap">
<style>
  :root {
    --bg: #e8e9eb;
    --navy: #333182;
    --red: #ed1c24;
    --white: #ffffff;
  }
  html, body {
    margin: 0;
    padding: 0;
    width: 1200px;
    height: 1000px;
    overflow: hidden;
    background: var(--bg);
    font-family: "Arimo", Arial, sans-serif;
  }
  .card {
    position: absolute;
    left: 193px;
    top: 233px;
    width: 844px;
    height: 520px;
    background: var(--navy);
    color: var(--white);
    font-weight: 700;
  }
  .contact-band {
    position: absolute;
    left: 0;
    top: 82px;
    width: 100%;
    height: 122px;
    background: var(--red);
    text-align: center;
  }
  .contact-phone {
    position: absolute;
    left: 0; right: 0;
    top: 22px;
    font-size: 38px;
    line-height: 1;
  }
  .contact-email {
    position: absolute;
    left: 0; right: 0;
    top: 68px;
    font-size: 31px;
    line-height: 1;
  }
  .services {
    position: absolute;
    margin: 0;
    padding: 0;
    list-style: none;
    font-size: 28px;
    line-height: 1;
  }
  .services li {
    position: absolute;
    white-space: nowrap;
  }
  .services li::before {
    content: "";
    position: absolute;
    left: -41px;
    top: 8px;
    width: 17px;
    height: 17px;
    background: var(--white);
  }
  .services-left { left: 171px; top: 287px; }
  .services-right { left: 472px; top: 287px; }
  .divider {
    position: absolute;
    left: 357px;
    top: 289px;
    width: 3px;
    height: 138px;
    background: var(--white);
  }
</style>
</head>
<body>
  <div class="card">
    <div class="contact-band">
      <div class="contact-phone">Phone 5074629183</div>
      <div class="contact-email">morvantgc@quellmail.com</div>
    </div>
    <ul class="services services-left">
      <li style="top:0">Roofing</li>
      <li style="top:47px">Siding</li>
      <li style="top:100px">Gutter</li>
    </ul>
    <div class="divider"></div>
    <ul class="services services-right">
      <li style="top:0">Additions</li>
      <li style="top:48px">Decks</li>
      <li style="top:100px">Handyman Services</li>
    </ul>
  </div>
</body>
</html>
```